Natural Cosmetics need a Packaging Design

We need a PACKAGING design for labels on hand/body wash bottles and soap paper boxes.
We target at high end markets.
We expect a contemporary and trendy design.
We don't need a separate logo. The brand name "Ma Vitrine" acts as the logo.
We want a modern and classic font for "Ma Vitrine".
Please see attached pictures for packaging samples.

Industry/Entity Type

Cosmetics

Requirements
Should not have
• a separate logo from the brand name

```html
<!DOCTYPE html>
<html lang="en">
<head>
<meta charset="utf-8">
<title>Ma Vitrine — Soap Box Packaging</title>
<link href="https://fonts.googleapis.com/css2?family=Montserrat:wght@400;500&display=swap" rel="stylesheet">
<style>
  :root {
    --paper: #ffffff;
    --teal: #16a89b;
    --teal-texture: #3cb2a7;
    --green: #8cc63e;
    --green-texture: #9dcf55;
    --ink-light: #ffffff;
    --brand: #15a398;
  }
  * { margin: 0; padding: 0; box-sizing: border-box; }
  html, body { width: 769px; height: 1200px; overflow: hidden; background: var(--paper); }
  body { font-family: "Montserrat", Arial, sans-serif; }
  .sheet { position: relative; width: 769px; height: 1200px; }

  .brand-header { position: absolute; left: 46px; top: 44px; color: var(--brand); }
  .brand-header__name { font-weight: 500; font-size: 46px; line-height: 1; letter-spacing: 0; }
  .brand-header__tagline { margin-top: 22px; font-size: 15px; font-weight: 500; letter-spacing: 3px; }

  .dieline { position: absolute; left: 0; width: 769px; height: 480px; }
  .dieline--teal { top: 120px; }
  .dieline--green { top: 626px; }

  .label { position: absolute; color: var(--ink-light); text-align: center; }
  .label__brand { font-weight: 500; font-size: 12px; line-height: 1; }
  .label__tagline { font-size: 5px; font-weight: 500; letter-spacing: 0.6px; margin-top: 4px; text-transform: uppercase; }
  .label__product { font-size: 10px; font-weight: 500; letter-spacing: 2px; line-height: 1.25; text-transform: uppercase; }
  .label__product--hero { font-size: 14px; letter-spacing: 2.6px; line-height: 1.3; }
  .label__note { font-size: 5.5px; font-weight: 500; letter-spacing: 0.5px; line-height: 1.35; text-transform: uppercase; }
  .label__copy { width: 84px; margin-left: auto; margin-right: auto; font-size: 6px; font-weight: 500; line-height: 1.25; }
</style>
</head>
<body>
<main class="sheet">

  <header class="brand-header">
    <div class="brand-header__name">Ma Vitrine</div>
    <div class="brand-header__tagline">PURE &amp; NATURAL</div>
  </header>

  <!-- Teal carton -->
  <svg class="dieline dieline--teal" viewBox="0 0 769 480">
    <g role="img" aria-label="Flowing teal wave texture covering the carton">
      <path fill="var(--teal-texture)" d="M58 125 H332 V55 H398 V441 H332 V370 H58 Q46 370 46 358 V137 Q46 125 58 125 Z"/>
      <path fill="var(--teal-texture)" d="M426 12 H623 Q647 12 647 36 V458 Q647 482 623 482 H426 Q402 482 402 458 V36 Q402 12 426 12 Z"/>
      <rect x="653" y="55" width="62" height="386" fill="var(--teal-texture)"/>
    </g>
    <rect x="158" y="125" width="104" height="245" fill="var(--teal)"/>
    <rect x="476" y="12" width="103" height="470" fill="var(--teal)"/>
  </svg>
  <div class="label" style="left:158px; top:300px; width:104px;">
    <div class="label__brand">Ma Vitrine</div>
    <div class="label__tagline">Pure &amp; Natural</div>
    <div class="label__note" style="margin-top:14px;">Gentle cleansing bar</div>
    <div class="label__copy" style="margin-top:13px;">a few lines about the product and ingredients will feature here. other mandatories will also appear here.</div>
  </div>
  <div class="label" style="left:476px; top:341px; width:103px;">
    <div class="label__brand">Ma Vitrine</div>
    <div class="label__tagline">Pure &amp; Natural</div>
    <div class="label__product label__product--hero" style="margin-top:19px;">Savon<br>Sans<br>Savon</div>
    <div class="label__note" style="margin-top:36px;">Gentle cleansing bar</div>
  </div>

  <!-- Green carton -->
  <svg class="dieline dieline--green" viewBox="0 0 769 480">
    <g role="img" aria-label="Flowing green wave texture covering the carton">
      <path fill="var(--green-texture)" d="M58 125 H332 V55 H398 V441 H332 V370 H58 Q46 370 46 358 V137 Q46 125 58 125 Z"/>
      <path fill="var(--green-texture)" d="M426 12 H623 Q647 12 647 36 V458 Q647 482 623 482 H426 Q402 482 402 458 V36 Q402 12 426 12 Z"/>
      <rect x="653" y="55" width="62" height="386" fill="var(--green-texture)"/>
    </g>
    <rect x="158" y="125" width="104" height="245" fill="var(--green)"/>
    <rect x="476" y="12" width="103" height="470" fill="var(--green)"/>
  </svg>
  <div class="label" style="left:158px; top:778px; width:104px;">
    <div class="label__brand">Ma Vitrine</div>
    <div class="label__tagline">Pure &amp; Natural</div>
    <div class="label__product" style="margin-top:11px;">Cucumber<br>Soap</div>
    <div class="label__copy" style="margin-top:3px;">a few lines about the product and ingredients will feature here. other mandatories will also appear here.</div>
  </div>
  <div class="label" style="left:476px; top:829px; width:103px;">
    <div class="label__brand">Ma Vitrine</div>
    <div class="label__tagline">Pure &amp; Natural</div>
    <div class="label__product" style="margin-top:20px;">Cucumber<br>Soap</div>
    <div class="label__note" style="margin-top:35px;">Gentle cleansing bar<br>with pure organic<br>sandalwood oil</div>
  </div>

</main>
</body>
</html>
```